Trash/recycling can & dumpster cleaning service

We power wash the inside and outside of trash/recycling cans & dumpsters. The water is collected and disposed of properly. We use environmentally safe products that leave your bins looking and smelling new.

Target Market(s)

Homeowners/renters, HOA's, Restaurant/Bars, Grocery stores, Hotel & Motels, Vacation homes, and neighborhoods with special rules to be allowed to live there.

Industry/Entity Type

Cleaning Service

Contact Information for Business Card

Brisk Bright Bins, Lyle Brennard-president-(608)517-4036, Martin Delacour-Vice President/treasurer-(608)862-1473, Madison, WI

Font styles to use
Serif

Requirements
Nice to have
• A picture of trash can (real or animated). The colors we would like to use is the same as the picture of Varo shoes in my images, sketches, or document section. Main color the aqua blue w/the bright fluorescent yellow and orange as accent colors.

```html
<!DOCTYPE html>
<html lang="en">
<head>
<meta charset="utf-8">
<title>Brisk Bright Bins — Business Card</title>
<link rel="stylesheet" href="https://fonts.googleapis.com/css2?family=Lora:wght@400;700&display=swap">
<style>
  :root {
    --backdrop: #e9e6e1;
    --card-white: #ffffff;
    --card-yellow: #fdb015;
    --brand-aqua: #1fb5c4;
    --accent-orange: #f7a21b;
    --accent-yellow: #e4d10f;
    --ink: #2b2b2b;
    --metal-light: #e6e6e6;
    --metal-dark: #8a8a8a;
    --gold-light: #c9a24a;
    --gold-dark: #7a6231;
    --shadow: rgba(0, 0, 0, 0.22);
  }
  * { box-sizing: border-box; margin: 0; padding: 0; }
  html, body {
    width: 1200px;
    height: 900px;
    overflow: hidden;
    background: var(--backdrop);
    font-family: "Lora", Georgia, serif;
  }
  .canvas {
    width: 1200px;
    height: 900px;
    display: flex;
    align-items: center;
    justify-content: center;
    gap: 60px;
  }
  .card {
    position: relative;
    width: 525px;
    height: 300px;
    border-radius: 18px;
    box-shadow: 0 10px 24px var(--shadow);
    overflow: hidden;
  }
  .card--front { background: var(--card-white); }
  .card--back {
    background: var(--card-yellow);
    display: flex;
    align-items: center;
    justify-content: center;
  }
  .card__band {
    position: absolute;
    left: 0;
    right: 0;
    top: 0;
    height: 8px;
    background: var(--brand-aqua);
  }
  .contacts {
    position: absolute;
    top: 40px;
    left: 290px;
    right: 24px;
    display: flex;
    flex-direction: column;
    gap: 22px;
  }
  .contact__name {
    color: var(--accent-orange);
    font-weight: 700;
    font-size: 17px;
    letter-spacing: 0.3px;
    text-transform: uppercase;
    line-height: 1.2;
  }
  .contact__role {
    color: var(--ink);
    font-size: 14px;
    margin-top: 3px;
    line-height: 1.25;
  }
  .contact__phone {
    display: flex;
    align-items: center;
    gap: 8px;
    color: var(--ink);
    font-size: 14px;
    margin-top: 8px;
  }
  .contact__phone svg { width: 16px; height: 16px; flex: none; }
  .brand {
    position: absolute;
    left: 36px;
    bottom: 30px;
    width: 240px;
    display: flex;
    flex-direction: column;
    align-items: flex-start;
    gap: 14px;
  }
  .brand__art {
    width: 200px;
    height: 115px;
    border-radius: 10px;
    background: linear-gradient(135deg, var(--metal-light), var(--metal-dark));
  }
  .brand__name {
    color: var(--brand-aqua);
    font-weight: 700;
    font-size: 19px;
    letter-spacing: 0.4px;
    text-transform: uppercase;
    white-space: nowrap;
  }
  .back__art {
    width: 340px;
    height: 190px;
    border-radius: 14px;
    background: linear-gradient(135deg, var(--gold-light), var(--gold-dark));
    opacity: 0.85;
  }
</style>
</head>
<body>
  <main class="canvas">
    <section class="card card--front" aria-label="Business card front">
      <div class="card__band"></div>
      <div class="contacts">
        <div class="contact">
          <p class="contact__name">Lyle Brennard</p>
          <p class="contact__role">President</p>
          <p class="contact__phone">
            <svg viewBox="0 0 24 24" aria-hidden="true">
              <path fill="#f7a21b" d="M6.6 10.8a15.1 15.1 0 0 0 6.6 6.6l2.2-2.2a1 1 0 0 1 1-.25 11.4 11.4 0 0 0 3.6.57 1 1 0 0 1 1 1V20a1 1 0 0 1-1 1A17 17 0 0 1 3 4a1 1 0 0 1 1-1h3.5a1 1 0 0 1 1 1c0 1.25.2 2.45.57 3.57a1 1 0 0 1-.25 1z"/>
            </svg>
            (608) 517 4036
          </p>
        </div>
        <div class="contact">
          <p class="contact__name">Martin Delacour</p>
          <p class="contact__role">Vice President / Treasurer</p>
          <p class="contact__phone">
            <svg viewBox="0 0 24 24" aria-hidden="true">
              <path fill="#f7a21b" d="M6.6 10.8a15.1 15.1 0 0 0 6.6 6.6l2.2-2.2a1 1 0 0 1 1-.25 11.4 11.4 0 0 0 3.6.57 1 1 0 0 1 1 1V20a1 1 0 0 1-1 1A17 17 0 0 1 3 4a1 1 0 0 1 1-1h3.5a1 1 0 0 1 1 1c0 1.25.2 2.45.57 3.57a1 1 0 0 1-.25 1z"/>
            </svg>
            (608) 862 1473
          </p>
        </div>
      </div>
      <div class="brand">
        <div class="brand__art" role="img" aria-label="Illustration of a silver trash can with its lid tipped open and crumpled paper inside"></div>
        <p class="brand__name">Brisk Bright Bins</p>
      </div>
    </section>
    <section class="card card--back" aria-label="Business card back">
      <div class="back__art" role="img" aria-label="Large gold-toned illustration of a trash can with lid tipped open"></div>
    </section>
  </main>
</body>
</html>
```